Business Card Ayurvedic Massage

I'm starting with my ayurvedic massage business and need a business card design. The design should be inline with my brand/logo as well as with the design of my website (www.lumo-thara.ch).
Front: logo and text "Ayurvedische Massagen"
back: name and adress (see details https://www.lumo-thara.ch/kontakt.html)

```html
<!DOCTYPE html>
<html lang="de">
<head>
<meta charset="utf-8">
<title>lumo-thara – Visitenkarte</title>
<link rel="stylesheet" href="https://fonts.googleapis.com/css2?family=Philosopher:wght@400;700&display=swap">
<style>
  :root {
    --stage: #f2efea;
    --maroon: #8c0f12;
    --maroon-deep: #6e0a0d;
    --gold: #e0a21f;
    --gold-light: #f3c451;
    --paper: #ececec;
    --paper-shade: #dcdcdc;
    --ink-red: #8e1616;
  }
  * { box-sizing: border-box; margin: 0; padding: 0; }
  html, body { width: 1200px; height: 852px; overflow: hidden; }
  body {
    background: var(--stage);
    font-family: "Philosopher", Georgia, serif;
    display: flex;
    align-items: center;
    justify-content: center;
    gap: 40px;
  }
  .card {
    position: relative;
    width: 540px;
    height: 350px;
    overflow: hidden;
    border-radius: 3px;
    box-shadow: 0 6px 18px rgba(0,0,0,.18);
  }

  /* Front */
  .card-front { background: var(--maroon); }
  .front-backdrop {
    position: absolute;
    left: 110px; top: 30px;
    width: 320px; height: 290px;
    background: radial-gradient(ellipse at center, var(--maroon-deep) 0%, rgba(110,10,13,0) 70%);
  }
  .front-ornament {
    position: absolute;
    width: 220px; height: 220px;
    border-radius: 50%;
    background: radial-gradient(circle, rgba(160,30,30,.35) 0%, rgba(160,30,30,0) 70%);
  }
  .front-ornament.top-right { right: -60px; top: -60px; }
  .front-ornament.bottom-left { left: -70px; bottom: -70px; }
  .front-brand {
    position: absolute;
    inset: 0;
    display: flex;
    flex-direction: column;
    align-items: center;
    justify-content: center;
    text-align: center;
  }
  .brand-name {
    display: flex;
    align-items: center;
    gap: 12px;
    color: var(--gold);
    font-weight: 700;
    font-size: 44px;
    letter-spacing: 1px;
  }
  .brand-dot {
    width: 14px; height: 14px;
    border-radius: 50%;
    background: var(--gold);
  }
  .brand-tagline {
    margin-top: 6px;
    color: var(--gold);
    font-size: 20px;
    letter-spacing: .5px;
  }

  /* Back */
  .card-back { background: var(--paper); }
  .back-pattern {
    position: absolute; inset: 0;
    background: linear-gradient(135deg, var(--paper) 0%, var(--paper-shade) 100%);
  }
  .back-mandala {
    position: absolute;
    left: -120px; top: 30px;
    width: 240px; height: 240px;
    border-radius: 50%;
    background: radial-gradient(circle, var(--gold-light) 0%, var(--gold) 35%, var(--ink-red) 60%, rgba(142,22,22,.15) 100%);
  }
  .back-content {
    position: absolute;
    left: 150px; right: 24px; top: 34px;
    text-align: center;
  }
  .back-brand {
    display: flex;
    align-items: center;
    justify-content: center;
    gap: 10px;
    color: var(--gold);
    font-weight: 700;
    font-size: 28px;
  }
  .back-brand .brand-dot { width: 10px; height: 10px; }
  .divider { display: block; margin: 14px auto; }
  .contact {
    font-style: normal;
    color: var(--ink-red);
    font-size: 18px;
    line-height: 1.32;
  }
</style>
</head>
<body>
  <section class="card card-front" aria-label="Vorderseite">
    <div class="front-ornament top-right" role="img" aria-label="Dezentes Mandala-Ornament"></div>
    <div class="front-ornament bottom-left" role="img" aria-label="Dezentes Mandala-Ornament"></div>
    <div class="front-backdrop" role="img" aria-label="Schattenhafte Silhouette eines indischen Palastes"></div>
    <div class="front-brand">
      <div class="brand-name"><span class="brand-dot"></span>lumo-thara</div>
      <div class="brand-tagline">Ayurvedische Massagen</div>
    </div>
  </section>

  <section class="card card-back" aria-label="Rückseite">
    <div class="back-pattern" role="img" aria-label="Heller grauer Damastgrund"></div>
    <div class="back-mandala" role="img" aria-label="Mandala-Ornament in Gold und Dunkelrot"></div>
    <div class="back-content">
      <div class="back-brand"><span class="brand-dot"></span>lumo-thara</div>
      <svg class="divider" width="230" height="16" viewBox="0 0 230 16" aria-hidden="true">
        <line x1="0" y1="8" x2="230" y2="8" stroke="#e0a21f" stroke-width="1.5"/>
        <ellipse cx="115" cy="8" rx="34" ry="6" fill="#8e1616" opacity=".75"/>
      </svg>
      <address class="contact">
        Mira Kestler, lumo-thara,<br>
        Lindenweg 12, 8853 Lachen (SZ)<br>
        info@lumo-thara.ch<br>
        +41 77 555 01 23 (Bitte keine Werbung)<br>
        www.lumo-thara.ch
      </address>
      <svg class="divider" width="230" height="16" viewBox="0 0 230 16" aria-hidden="true">
        <line x1="0" y1="8" x2="230" y2="8" stroke="#e0a21f" stroke-width="1.5"/>
        <ellipse cx="115" cy="8" rx="34" ry="6" fill="#8e1616" opacity=".75"/>
      </svg>
    </div>
  </section>
</body>
</html>
```